Business Card Design Project - velmora

We are building an agency for innovative solutions in marketing, education and events to pharmaceutical companies, physicians, medical societies, patient advocacy groups. We want to become a reference in this market in Brazil as the most boutique agency here. We deal with every detail with a lot of love and caring for what we do like craftsmen.
Our card must show innovation and inspiration. Yet should be clean. Something like Swiss design, quint design, etc.
Reason: I think the initial time was too short. I believe with more time you can exceed expectations. I'm liking a lot this experience
Target Market(s)
Pharmaceutical companies, doctors and patients
Industry/Entity Type
Pharmaceutical
Font styles to use
Other font styles liked:
- Helvetia family
Colors
Designer to choose colors to be used in the design.
Requirements
Must have
- Modern, clean,
Nice to have
- Innovative idea to show
Should not have
- Not too appear too much Comercial. Must be modern but sober.

```html
<!DOCTYPE html>
<html lang="en">
<head>
<meta charset="utf-8">
<title>velmora – business card</title>
<link rel="stylesheet" href="https://fonts.googleapis.com/css2?family=Inter:wght@200;300;400&display=swap">
<style>
  :root {
    --brand-blue: #0041a3;
    --brand-sky: #3aa9ec;
    --mark-blue: #1f4fae;
    --paper: #ffffff;
    --muted-text: #aebfe2;
    --edge: #c9c9c9;
    --shadow: #c8c8c8;
    --band-light: #a9a9a9;
    --band-dark: #7c7c7c;
  }
  * { margin: 0; padding: 0; box-sizing: border-box; }
  html, body { width: 1200px; height: 900px; overflow: hidden; background: var(--paper); }
  body { font-family: "Inter", Helvetica, Arial, sans-serif; position: relative; }

  .card { position: absolute; }

  /* Front */
  .card-front {
    left: 360px; top: 94px; width: 464px; height: 273px;
    background: var(--brand-blue);
  }
  .wordmark {
    position: absolute; left: 0; right: 0;
    text-align: center; font-weight: 200; letter-spacing: 0.02em;
  }
  .card-front .wordmark {
    top: 102px; color: var(--brand-sky); font-size: 26px; line-height: 32px;
  }
  .website {
    position: absolute; left: 0; right: 0; top: 172px;
    text-align: center; color: var(--paper);
    font-size: 10px; font-weight: 300; letter-spacing: 0.02em;
  }

  /* Back */
  .card-back-shadow {
    left: 363px; top: 464px; width: 465px; height: 274px;
    background: var(--shadow);
  }
  .card-back {
    left: 355px; top: 456px; width: 465px; height: 274px;
    display: flex; border: 1px solid var(--edge);
    background: var(--paper);
  }
  .details-panel {
    width: 290px; height: 100%; background: var(--brand-blue);
    position: relative; color: var(--paper); text-align: right;
  }
  .holder { position: absolute; right: 31px; top: 85px; font-size: 13px; line-height: 15px; font-weight: 300; }
  .contact { position: absolute; right: 31px; top: 154px; font-size: 12px; line-height: 18px; font-weight: 300; color: var(--muted-text); }
  .contact li { list-style: none; display: flex; justify-content: flex-end; align-items: center; gap: 6px; }
  .contact svg { fill: var(--paper); }
  .mark-panel { flex: 1; position: relative; }
  .mark-panel .wordmark { top: 122px; color: var(--mark-blue); font-size: 22px; line-height: 28px; }

  .presentation-band {
    position: absolute; left: 0; top: 788px; width: 1200px; height: 112px;
    background: linear-gradient(90deg, var(--band-light), var(--band-dark) 50%, var(--band-light));
  }
</style>
</head>
<body>
  <section class="card card-front">
    <p class="wordmark">velmora</p>
    <p class="website">www.velmora.com</p>
  </section>

  <div class="card card-back-shadow"></div>
  <section class="card card-back">
    <div class="details-panel">
      <p class="holder">Lucas Moreno<br>CEO</p>
      <ul class="contact">
        <li>27 Harbor ave. 20871 - Fla</li>
        <li>
          <svg width="7" height="11" viewBox="0 0 7 11" aria-hidden="true"><rect x="0" y="0" width="7" height="11" rx="1"/></svg>
          1-40258316
        </li>
        <li>
          <svg width="8" height="6" viewBox="0 0 8 6" aria-hidden="true"><rect x="0" y="0" width="8" height="6"/></svg>
          lucas@velmora.com
        </li>
      </ul>
    </div>
    <div class="mark-panel">
      <p class="wordmark">velmora</p>
    </div>
  </section>

  <div class="presentation-band" role="img" aria-label="Brushed grey metal texture band"></div>
</body>
</html>
```